Pawlane Website

website will need to have the following features:
• Photo Galleries of each species (Dogs, Cats, Birds, Fish, Reptiles, Rabbits) in a light box popup
o Each species may have several different categories for example:
 Fish
• Marine fish
• Fresh water
• tropical
• Cichlid
• Information Fact sheets of each species – Downloaded as a pdf which can be either
o Care Sheets
o Training Sheets
• Members Area
o Username (Email Address) & Password login
o New signups
o Exclusive Member Deals
o Newsletter options

The front page must be very simple (for example lumavest.com.au) contain the following:
• Product of the week - which can be purchased online
o Short details
o Cost
• Pet Club Sign up picture
• Animal of the week/month
• Contact Phone Number and addresses of the stores
• A jQuery slideshow (Images could include stores, pets etc…)
The main page MUST keep simple. We do not want it cluttered.

Inner Page
The animals / reptile page will need to have:
• Short description of the species
• Photo Galleries
• A list of what is in stock and the list needs to clearly be sorted by each store (Use of Tabs maybe).
• Facts sheets / Info sheets
The type of website ideas (not the type of look that we are necessary after) is and the sort of content that we want to offer are as follows:

http://www.scalenook.com.au/
http://www.brindlecovepaws.com.au/
http://www.thefurrowden.com.au
http://www.tailtown.net.au

Colour in the new website:
Blue
Red
Grey
Yellow

Original site:

http://www.critterglow.com.au
Updates

Hi Guys,

We had feedback from the client and they would like to see a few dark designs.

Thanks                                   

Reason: We would like to reopen this contest back up for a further week

Target Market(s)

Targeting animal lovers

Industry/Entity Type

Store

Requirements
Should not have
• Alter the logo in anyway

```html
<!DOCTYPE html>
<html lang="en">
<head>
<meta charset="utf-8">
<title>Pawlane – Home</title>
<link rel="stylesheet" href="https://fonts.googleapis.com/css2?family=Jost:wght@400;500&family=Noto+Sans:ital,wght@0,400;0,700;1,700&display=swap">
<style>
:root{
  --bg:#e2e2e2;
  --bg-band:#e9e9e9;
  --page:#ffffff;
  --blue:#1a9be6;
  --blue-dark:#1c6fb5;
  --nav:#2a8fd6;
  --red:#e0141e;
  --text:#4a4a4a;
  --panel:#cdcdcd;
  --field:#f6f6f6;
  --rule:#dedede;
  --wave:#e6f1fb;
}
*{margin:0;padding:0;box-sizing:border-box}
html,body{width:1200px;height:687px;overflow:hidden}
body{
  position:relative;
  background:linear-gradient(var(--bg) 0,var(--bg) 85px,var(--bg-band) 85px,var(--bg) 240px);
  font-family:"Noto Sans",Verdana,sans-serif;
  color:var(--text);
}
.page{position:absolute;left:176px;top:122px;width:851px;height:565px;background:var(--page)}
.wave{position:absolute;left:0;top:70px}
.brand{position:absolute;left:31px;top:36px;font-family:"Jost",sans-serif;font-weight:400;color:var(--blue);font-size:30px;line-height:1}
.nav{position:absolute;left:148px;top:63px;display:flex;font-family:"Jost",sans-serif;font-size:15px;color:var(--nav);list-style:none}
.nav li{padding:0 19px;border-left:1px solid #dfe6ec;line-height:21px}
.nav li:first-child{border-left:0;padding-left:0;font-weight:500;color:var(--blue-dark)}
.account{position:absolute;right:52px;top:47px;text-align:right;font-size:10px;color:#555;line-height:17px}
.account b{color:var(--blue-dark);font-style:italic}
.social{display:inline-block;width:24px;height:24px;border-radius:3px;background:#3b5b9c;vertical-align:middle;margin-left:3px}
.signup{position:absolute;left:21px;top:153px;width:96px;height:232px;background:var(--panel);border-radius:7px;box-shadow:2px 3px 4px rgba(0,0,0,.2);padding:14px 9px}
.signup h3{font-size:10px;color:var(--blue-dark);font-weight:400;margin-bottom:13px}
.signup label{display:block;font-size:9px;color:#222;line-height:11px}
.signup .field{height:11px;background:var(--field);border-radius:2px;margin:2px 0 11px;box-shadow:inset 0 1px 2px rgba(0,0,0,.15)}
.signup .btn{margin:20px 0 0 8px;width:62px;height:28px;border-radius:6px;background:linear-gradient(#5aa9e8,#1d5fab);color:#fff;font-size:12px;font-weight:700;display:flex;align-items:center;justify-content:center;gap:3px;box-shadow:0 2px 3px rgba(0,0,0,.25)}
.club-photo{position:absolute;left:21px;top:400px;width:96px;height:141px;border-radius:6px;background:linear-gradient(#8b7d72,#e8e6ea 60%,#b9b3bb);box-shadow:2px 3px 4px rgba(0,0,0,.2)}
.divider{position:absolute;left:131px;top:150px;width:1px;height:415px;background:var(--rule)}
.slideshow{position:absolute;left:148px;top:121px;width:430px;height:171px;border-radius:6px;background:linear-gradient(180deg,#050505 0,#0c0c10 45%,#5b4a52 75%,#b27a5e 100%);box-shadow:0 2px 4px rgba(0,0,0,.25)}
.slideshow svg{position:absolute;top:78px}
.heading{position:absolute;font-family:"Jost",sans-serif;font-size:15px;color:var(--red);font-weight:400}
.about{position:absolute;left:150px;top:350px;width:440px;font-size:12.3px;line-height:17px}
.about p{margin-bottom:17px}
.about ul{list-style:none;margin:-17px 0 17px}
.about li::before{content:"";display:inline-block;width:10px;height:7px;margin:0 4px 1px 4px;background:var(--blue-dark);clip-path:polygon(0 30%,55% 30%,55% 0,100% 50%,55% 100%,55% 70%,0 70%)}
.gallery{position:absolute;left:604px;top:153px;display:grid;grid-template-columns:96px 96px;gap:11px 13px}
.thumb{height:77px;box-shadow:1px 2px 3px rgba(0,0,0,.25)}
.t-fish{background:linear-gradient(135deg,#9bb087,#3a6fc8 55%,#b8c08f)}
.t-cat{background:radial-gradient(circle at 50% 45%,#e8b88a,#f1ece8 70%)}
.t-snake{background:linear-gradient(135deg,#1f3a1a,#7fc43a 55%,#2d4a1e)}
.t-tortoise{background:radial-gradient(circle at 50% 50%,#9a7a42,#1c1a16 75%)}
.more{position:absolute;left:753px;top:350px;font-size:10.5px;font-style:italic;font-weight:700;color:var(--blue)}
.contact{position:absolute;left:604px;top:401px;font-size:12.3px;line-height:17px;color:var(--blue)}
.contact p+p{margin-top:17px}
</style>
</head>
<body>
<div class="page">
  <svg class="wave" width="851" height="90" viewBox="0 0 851 90" aria-hidden="true">
    <path d="M0 90 C60 40 150 35 320 40 C480 45 600 50 700 35 C760 25 810 20 851 10 L851 0 C780 30 640 42 480 38 C300 30 120 20 0 50 Z" fill="var(--wave)"/>
  </svg>
  <div class="brand">Pawlane</div>
  <ul class="nav">
    <li>Home</li><li>Photo Gallery</li><li>Pets</li><li>Membership</li><li>Newsletter</li>
  </ul>
  <div class="account"><b>Log in</b> or <b>Sign up</b> here<br>find us on <span class="social"></span></div>

  <form class="signup">
    <h3>Sign up</h3>
    <label>Name</label><div class="field"></div>
    <label>Surname</label><div class="field"></div>
    <label>Email</label><div class="field"></div>
    <label>Password</label><div class="field"></div>
    <div class="btn">Sign Up <svg width="6" height="8"><path d="M0 0L6 4L0 8Z" fill="#fff"/></svg></div>
  </form>
  <div class="club-photo" role="img" aria-label="Photo of a groomed white poodle for the pet club"></div>
  <div class="divider"></div>

  <div class="slideshow" role="img" aria-label="Slideshow photo of a tropical reef aquarium with colourful fish">
    <svg style="left:7px" width="10" height="18"><path d="M10 0L0 9L10 18Z" fill="#fff"/></svg>
    <svg style="right:9px" width="10" height="18"><path d="M0 0L10 9L0 18Z" fill="#fff"/></svg>
  </div>

  <h2 class="heading" style="left:148px;top:342px">About us</h2>
  <div class="about" style="top:370px">
    <p>Lorem ipsum dolor sit amet, consectetuer adipiscing elit, sed diam nonummy nibh euismod tincidunt ut laoreet dolore magna aliquam erat volutpat. Ut wisi enim ad minim veniam,</p>
    <p>quis nostrud exerci tation ullamcorper suscipit lobortis nisl ut aliquip ex ea commodo consequat. Duis autem vel eum iriure:</p>
    <ul><li>dolor in hendrerit</li><li>in vulputate velit esse</li><li>molestie consequat, vel</li><li>illum dolore eu feugiat</li></ul>
    <p>nulla facilisis at vero eros et accumsan et iusto odio dignissim qui</p>
  </div>

  <h2 class="heading" style="left:605px;top:134px">Photo Gallery</h2>
  <div class="gallery">
    <div class="thumb t-fish" role="img" aria-label="Blue striped tang fish"></div>
    <div class="thumb t-cat" role="img" aria-label="Ginger kitten"></div>
    <div class="thumb t-snake" role="img" aria-label="Green tree snake"></div>
    <div class="thumb t-tortoise" role="img" aria-label="Tortoise"></div>
  </div>
  <div class="more">View more</div>

  <h2 class="heading" style="left:605px;top:396px">Contact us</h2>
  <div class="contact" style="top:424px">
    <p>224 Lorem ipsum dolor<br>Loremeiem igfiapsum dolor 4122<br>Lorem ipsum dolorl 1800 555 019<br>Or +61 (0)7 5550 1274</p>
    <p>224 Lorem ipsum dolor<br>Loremeiem igfiapsum dolor 4122<br>Lorem ipsum dolorl 1800 555 019<br>Or +61 (0)7 5550 1274</p>
  </div>
</div>
</body>
</html>
```